Briefpapier im Word-Format für Sachverständigenbüro
Zielgruppe
Sachverständigenbüro für Sach- und Haftpflichtversicherungsschäden
Aufgabenstellung
Beibehaltung aktueller Logos, Erstellung einer Word-Datei zum selbst ausdrucken und kompatibel für Ausdruck über Word ohne Abschnitt der Seitenränder

```html
<!DOCTYPE html>
<html lang="de">
<head>
<meta charset="utf-8">
<title>Briefbogen Gutachtenbüro Weststern</title>
<link href="https://fonts.googleapis.com/css2?family=Open+Sans:wght@400;600&display=swap" rel="stylesheet">
<style>
  :root {
    --bg: #d2d2d2;
    --paper: #f7f7f7;
    --red: #c8232a;
    --ink: #3a3a3a;
    --ink-dark: #1e1e1e;
    --pill: #3b3a3c;
  }
  * { box-sizing: border-box; margin: 0; padding: 0; }
  html, body { width: 1166px; height: 1200px; overflow: hidden; background: var(--bg); }
  body { font-family: "Open Sans", Arial, sans-serif; color: var(--ink); position: relative; }

  .letterhead {
    position: absolute; left: 173px; top: 20px;
    width: 820px; height: 1160px;
    background: var(--paper);
    box-shadow: 0 10px 30px rgba(0,0,0,.18);
    overflow: hidden;
  }
  .rule-top {
    position: absolute; left: 24px; right: 24px; top: 28px;
    height: 7px; background: var(--red);
  }
  .brand {
    position: absolute; right: 60px; top: 110px;
    display: flex; align-items: center; gap: 10px;
    font-size: 22px; font-weight: 600; color: var(--ink-dark);
    white-space: nowrap;
  }
  .brand-mark { width: 16px; height: 16px; background: var(--red); }

  .contact {
    position: absolute; left: 570px; top: 160px;
    border-left: 2px solid var(--red);
    padding: 4px 0 4px 14px;
    font-size: 13.5px; line-height: 19px; color: var(--ink-dark);
    white-space: nowrap;
  }
  .contact .accent { color: var(--red); }
  .contact-row { display: flex; align-items: center; gap: 8px; }
  .contact-row svg { width: 11px; height: 11px; fill: var(--red); flex: none; }
  .owner {
    position: absolute; left: 566px; top: 290px;
    font-size: 13.5px; color: var(--ink-dark); white-space: nowrap;
  }

  .sender {
    position: absolute; left: 80px; top: 160px;
    font-size: 10px; color: var(--ink-dark);
    border-bottom: 1px solid var(--ink-dark); padding-bottom: 1px;
    white-space: nowrap;
  }
  .sender .accent { color: var(--red); }
  .recipient {
    position: absolute; left: 80px; top: 182px;
    font-size: 15.5px; line-height: 22px; font-style: normal;
  }

  .fold-mark { position: absolute; left: 20px; width: 14px; height: 1.5px; background: var(--ink-dark); }
  .fold-1 { top: 392px; }
  .fold-2 { top: 780px; }

  .body-copy {
    position: absolute; left: 80px; right: 60px; top: 400px;
    font-size: 15px; line-height: 22px; text-align: justify;
  }
  .body-copy p { margin-bottom: 14px; }

  .footer {
    position: absolute; left: 24px; right: 24px; bottom: 40px;
    display: flex; align-items: flex-end; gap: 8px;
  }
  .footer-rule { height: 7px; background: var(--red); margin-bottom: 0; }
  .footer-rule.long { flex: 1; }
  .footer-rule.short { width: 70px; flex: none; }
  .footer-web {
    flex: none;
    height: 34px; padding: 0 16px; border-radius: 8px;
    background: var(--pill); color: #fff;
    font-size: 14px; line-height: 34px; white-space: nowrap;
  }
</style>
</head>
<body>
  <main class="letterhead">
    <div class="rule-top"></div>

    <div class="brand"><span class="brand-mark"></span>Gutachtenbüro Weststern</div>

    <div class="contact">
      <div>Gutachtenbüro <span class="accent">Weststern</span></div>
      <div>Handwerkerhof 7</div>
      <div>86001 Birkenfelde</div>
      <div class="contact-row">
        <svg viewBox="0 0 24 24" aria-hidden="true"><path d="M6.6 10.8a15 15 0 0 0 6.6 6.6l2.2-2.2a1 1 0 0 1 1-.25 11.4 11.4 0 0 0 3.6.57 1 1 0 0 1 1 1V20a1 1 0 0 1-1 1A17 17 0 0 1 3 4a1 1 0 0 1 1-1h3.5a1 1 0 0 1 1 1c0 1.25.2 2.45.57 3.6a1 1 0 0 1-.25 1z"/></svg>
        04412 / 5550181
      </div>
      <div class="contact-row">
        <svg viewBox="0 0 24 24" aria-hidden="true"><path d="M6 3h10v5H6zM4 9h16a2 2 0 0 1 2 2v6h-4v4H6v-4H2v-6a2 2 0 0 1 2-2zm4 7v3h8v-3z"/></svg>
        04412 / 5550182
      </div>
      <div class="contact-row">
        <svg viewBox="0 0 24 24" aria-hidden="true"><path d="M2 5h20v14H2zm2 2v.5l8 5 8-5V7z"/></svg>
        post@gutachten-weststern.de
      </div>
    </div>
    <div class="owner">Inhaber: Henrik Lauterbach</div>

    <div class="sender">Gutachtenbüro <span class="accent">Weststern</span> <span class="accent">|</span> Handwerkerhof 7 <span class="accent">|</span> 86001 Birkenfelde</div>
    <address class="recipient">
      Mustermann GmbH<br>
      Herr Max Mustermann<br>
      Musterstraße 4711<br>
      08159 Musterstadt
    </address>

    <div class="fold-mark fold-1"></div>
    <div class="fold-mark fold-2"></div>

    <section class="body-copy">
      <p>Lorem ipsum dolor sit amet, consetetur sadipscing elitr, sed diam nonumy eirmod tempor invidunt ut labore et dolore magna aliquyam erat, sed diam voluptua. At vero eos et accusam et justo duo dolores et ea rebum. Stet clita kasd gubergren, no sea takimata sanctus est Lorem ipsum dolor sit amet.</p>
      <p>Lorem ipsum dolor sit amet, consetetur sadipscing elitr, sed diam nonumy eirmod tempor invidunt ut labore et dolore magna aliquyam erat, sed diam voluptua. At vero eos et accusam et justo duo dolores et ea rebum. Stet clita kasd gubergren, no sea takimata sanctus est Lorem ipsum dolor sit amet. Lorem ipsum dolor sit amet, consetetur sadipscing elitr, sed diam nonumy eirmod tempor.</p>
      <p>Invidunt ut labore et dolore magna aliquyam erat, sed diam voluptua. At vero eos et accusam et justo duo dolores et ea rebum. Stet clita kasd gubergren, no sea takimata sanctus est Lorem ipsum dolor sit amet. Lorem ipsum dolor sit amet, consetetur sadipscing elitr, sed diam nonumy eirmod tempor invidunt ut labore et dolore magna aliquyam erat, sed diam voluptua.</p>
      <p>At vero eos et accusam et justo duo dolores et ea rebum. Stet clita kasd gubergren, no sea takimata sanctus est Lorem ipsum dolor sit amet.</p>
    </section>

    <footer class="footer">
      <div class="footer-rule long"></div>
      <div class="footer-web">www.gutachten-weststern.de</div>
      <div class="footer-rule short"></div>
    </footer>
  </main>
</body>
</html>
```